Signboard menu for a Fastfood takeaway shop

My current signboard menu is old now, I want to upgrade to a new, bigger and brighter signboard menu.
Photos of the old menu attached but there are some changes in each sections of the menu needs to be changed.
Size of the signboard :
L: 1700cm
H: 1200cm

Industry/Entity Type

Fastfood Hospitality

Colors
FFC000
F8CF3A
FAE287
FDF2CF
FEFAEE

```html
<!DOCTYPE html>
<html lang="en">
<head>
<meta charset="utf-8">
<title>Takeaway Menu Board</title>
<link href="https://fonts.googleapis.com/css2?family=Fira+Sans:wght@400;500;700&display=swap" rel="stylesheet">
<style>
:root{
  --board-deep:#780000;
  --board-mid:#a30b12;
  --board-hot:#cc161d;
  --cream:#fde9b8;
  --cream-text:#fdeccb;
  --title-red:#c8102e;
  --page:#ffffff;
}
*{margin:0;padding:0;box-sizing:border-box}
html,body{width:1200px;height:988px;overflow:hidden;background:var(--page)}
.menu-board{
  position:absolute;left:21px;top:49px;width:1929px;height:1361px;
  transform:scale(0.6);transform-origin:top left;
  background:radial-gradient(ellipse at 50% 50%,var(--board-hot) 0%,var(--board-mid) 45%,var(--board-deep) 100%);
  font-family:"Fira Sans",sans-serif;color:var(--cream-text);
}
.section{position:absolute;width:605px;border:3px solid var(--cream);border-radius:22px;overflow:hidden}
.section-title{
  height:72px;background:var(--cream);color:var(--title-red);
  font-weight:700;font-size:33px;line-height:72px;text-align:center;letter-spacing:.3px;
}
.row{position:absolute;left:0;width:100%;height:32px}
.row span{position:absolute;top:0;font-weight:500;font-size:26px;line-height:32px;white-space:nowrap}
.small span{font-size:24px}
.note{position:absolute;font-weight:400;font-size:22px;line-height:24px;white-space:nowrap}
.sub-title{position:absolute;left:0;width:100%;text-align:center;font-weight:700;font-size:32px;line-height:36px}
</style>
</head>
<body>
<div class="menu-board">

  <!-- Column 1 -->
  <section class="section" style="left:18px;top:21px;height:485px">
    <h2 class="section-title">SANDWICHES</h2>
    <div class="row" style="top:86px"><span style="left:25px">MALT SPREAD</span><span style="left:204px">$ 4.50</span><span style="left:319px">SAUSAGE</span><span style="left:498px">$ 7.00</span></div>
    <div class="row" style="top:136px"><span style="left:25px">CHEESE</span><span style="left:204px">$ 4.50</span><span style="left:319px">SCALLOP</span><span style="left:498px">$ 6.00</span></div>
    <div class="row" style="top:186px"><span style="left:25px">TOMATO</span><span style="left:204px">$ 4.50</span><span style="left:319px">CHIP</span><span style="left:498px">$ 6.00</span></div>
    <div class="row" style="top:236px"><span style="left:25px">SALAD</span><span style="left:204px">$ 7.00</span><span style="left:319px">BACON</span><span style="left:498px">$ 6.00</span></div>
    <div class="row" style="top:286px"><span style="left:25px">HAM</span><span style="left:204px">$ 7.50</span><span style="left:319px">BACON / EGG</span><span style="left:498px">$ 6.00</span></div>
    <div class="row" style="top:337px"><span style="left:25px">CHICKEN</span><span style="left:204px">$ 7.50</span><span style="left:319px">SHNITZEL</span><span style="left:498px">$ 8.50</span></div>
    <div class="row" style="top:387px"><span style="left:25px">ROAST BEEF</span><span style="left:204px">$ 7.50</span><span style="left:319px">ROLL</span><span style="left:498px">$ 0.50</span></div>
    <div class="row" style="top:438px"><span style="left:25px">RISSOLE</span><span style="left:204px">$ 7.50</span></div>
  </section>

  <section class="section" style="left:18px;top:526px;height:429px">
    <h2 class="section-title">SALAD IN TUBS</h2>
    <div class="row small" style="top:86px"><span style="left:25px">PLAIN SALAD $ 7.50</span><span style="left:270px">CAESAR SALAD TUB</span><span style="left:512px">$10.00</span></div>
    <div class="sub-title" style="top:129px">EXTRA</div>
    <div class="row small" style="top:174px"><span style="left:25px">PINEAPPLE</span><span style="left:178px">$ 1.00</span><span style="left:332px">BACON/ MEAT</span><span style="left:512px">$2.50</span></div>
    <div class="row small" style="top:216px"><span style="left:25px">SAUCE $ 0.50</span><span style="left:395px">EGG</span><span style="left:512px">$1.50</span></div>
    <div class="row small" style="top:256px"><span style="left:25px">AVOCADO/ CHEESE $ 1.20</span></div>
    <div class="row small" style="top:297px"><span style="left:25px">TOMATO/BEETROOT ONION/CUCUMBER</span><span style="left:512px">$0.50</span></div>
    <div class="row small" style="top:338px"><span style="left:25px">KEBAB MEAT:</span></div>
    <div class="row small" style="top:374px"><span style="left:25px">CHICKEN 100gr</span><span style="left:229px">$ 3.50</span><span style="left:352px">LAMB 100gr</span><span style="left:512px">$4.50</span></div>
  </section>

  <section class="section" style="left:18px;top:975px;height:364px">
    <h2 class="section-title">BURGERS (BEEF OR CHICKEN)</h2>
    <div class="row small" style="top:86px"><span style="left:25px">PLAIN</span><span style="left:164px">$ 7.00</span><span style="left:252px">WORKS</span><span style="left:512px">$10.00</span></div>
    <div class="row small" style="top:127px"><span style="left:25px">CHEESE</span><span style="left:164px">$ 8.00</span><span style="left:252px">BACON/ CHEESE</span><span style="left:512px">$9.00</span></div>
    <div class="row small" style="top:168px"><span style="left:25px">MEGA</span><span style="left:512px">$ 15.00</span></div>
    <p class="note" style="left:25px;top:202px">Works Burger With Double Meat, Double Bacon And Egg</p>
    <div class="row small" style="top:237px"><span style="left:25px">SCHNITZEL BURGERS EXTRA</span><span style="left:512px">$1.50</span></div>
    <div class="row small" style="top:278px"><span style="left:25px">HAWAIIAN <span style="position:static;font-weight:400;font-size:22px">Works burger with Pineapple</span></span><span style="left:512px">$10.00</span></div>
    <div class="row small" style="top:319px"><span style="left:25px">MEXICAN</span><span style="left:164px">$ 8.00</span><span style="left:252px">BACON/EGG BURGER</span><span style="left:512px">$9.50</span></div>
  </section>

  <!-- Column 2 -->
  <section class="section" style="left:662px;top:21px;height:210px">
    <h2 class="section-title">BACON/EGG ROLL or WRAPS</h2>
    <div class="row small" style="top:86px"><span style="left:26px">BACON/EGG</span><span style="left:179px">$7.00</span><span style="left:258px">BACON/EGG/CHEESE</span><span style="left:513px">$8.20</span></div>
    <div class="row small" style="top:124px"><span style="left:26px">BACON/EGG/CHEESE/ONION</span><span style="left:513px">$9.20</span></div>
    <div class="row small" style="top:162px"><span style="left:26px">WRAPS: EXTRA</span><span style="left:513px">$3.00</span></div>
  </section>

  <section class="section" style="left:662px;top:241px;height:240px">
    <h2 class="section-title">GRAVY ROLL</h2>
    <div class="row small" style="top:87px"><span style="left:26px">SLOW COOK BEEF</span><span style="left:513px">$8.50</span></div>
    <div class="row small" style="top:118px"><span style="left:26px">SLOW COOK PORK</span><span style="left:513px">$8.00</span></div>
    <div class="row small" style="top:158px"><span style="left:26px">RISSOLE</span><span style="left:179px">$8.00</span><span style="left:362px">SAUSAGE</span><span style="left:513px">$7.00</span></div>
    <div class="row small" style="top:193px"><span style="left:26px">SCHNITZEL</span><span style="left:179px">$8.00</span><span style="left:362px">CHIPS</span><span style="left:513px">$6.50</span></div>
  </section>

  <section class="section" style="left:662px;top:491px;height:134px">
    <h2 class="section-title">KEBABS</h2>
    <div class="row small" style="top:83px"><span style="left:26px">CHICKEN&nbsp; $8.00</span><span style="left:252px">LAMB $14.50</span><span style="left:449px">MIX $14.50</span></div>
  </section>

  <section class="section" style="left:662px;top:635px;height:351px">
    <h2 class="section-title">SCHNITZEL WRAPS</h2>
    <div class="row small" style="top:78px"><span style="left:26px">CAESAR</span><span style="left:145px">$12.00</span><span style="left:269px">SALAD AND CHEESE</span><span style="left:513px">$11.00</span></div>
    <div class="row small" style="top:114px"><span style="left:26px">WORKS</span><span style="left:513px">$8.50</span></div>
    <p class="note" style="left:26px;top:146px">With Bacon, Egg, Cheese And All Salad</p>
    <div class="row small" style="top:176px"><span style="left:26px">MEXICAN</span><span style="left:513px">$8.50</span></div>
    <p class="note" style="left:26px;top:208px">Mexican spiced Schnitzel with Lettuce, Tomato, Spanish<br>onion, Cheese, Sour Cream and Hot chilli sauce</p>
    <div class="row small" style="top:261px"><span style="left:26px">HAWAIIAN</span><span style="left:513px">$8.50</span></div>
    <p class="note" style="left:26px;top:293px">with Bacon, Lettuce, Tomato, Pineapple, Cheese with<br>Honey mustard</p>
  </section>

  <section class="section" style="left:662px;top:997px;height:134px">
    <h2 class="section-title">SNACK PACKS</h2>
    <div class="row small" style="top:83px"><span style="left:26px">CHICKEN&nbsp; $13.00</span><span style="left:252px">LAMB $15.00</span><span style="left:449px">MIX $15.00</span></div>
  </section>

  <section class="section" style="left:662px;top:1141px;height:198px">
    <h2 class="section-title">BIG BREAKY (SPECIAL)</h2>
    <div class="row small" style="top:86px"><span style="left:26px">BACON, 2X EGGS, SAUSAGE, FRIED</span></div>
    <div class="row small" style="top:115px"><span style="left:26px">TOMATO, HASHBROWN AND TOAST</span></div>
    <div class="row small" style="top:100px"><span style="left:513px">$15.00</span></div>
    <div class="row small" style="top:153px"><span style="left:26px">WITH A SMALL COFFEE</span><span style="left:513px">$17.00</span></div>
  </section>

  <!-- Column 3 -->
  <section class="section" style="left:1306px;top:21px;height:570px">
    <h2 class="section-title">HOT FOOD</h2>
    <div class="row" style="top:86px"><span style="left:26px">SCALLOP</span><span style="left:218px">$3.00</span><span style="left:302px">CHICKEN STICK</span><span style="left:509px">$4.70</span></div>
    <div class="row" style="top:135px"><span style="left:26px">DIM SIM</span><span style="left:218px">$3.00</span><span style="left:302px">VEGGIE ROLL</span><span style="left:509px">$4.50</span></div>
    <div class="row" style="top:184px"><span style="left:26px">HASH BROWN</span><span style="left:218px">$3.50</span><span style="left:302px">SPRING ROLL</span><span style="left:509px">$4.50</span></div>
    <div class="row" style="top:233px"><span style="left:26px">SAUSAGE</span><span style="left:218px">$4.00</span><span style="left:302px">BATTERED SAV</span><span style="left:509px">$4.50</span></div>
    <div class="row" style="top:282px"><span style="left:26px">CORN FRITTER</span><span style="left:218px">$4.70</span><span style="left:302px">CORN DOG</span><span style="left:509px">$5.50</span></div>
    <div class="row" style="top:331px"><span style="left:26px">MINI CHICKEN DIM SIM</span><span style="left:509px">$4.00</span></div>
    <div class="row" style="top:380px"><span style="left:26px">ROAST BEEF</span><span style="left:218px">$7.50</span></div>
    <div class="row" style="top:429px"><span style="left:26px">CHIPS:</span></div>
    <div class="row small" style="top:463px"><span style="left:26px">SMALL $8.00</span><span style="left:203px">MEDIUM $14.50</span><span style="left:413px">LARGE $14.50</span></div>
    <div class="row" style="top:512px"><span style="left:26px">GRAVY: EXTRA $2.00</span></div>
  </section>

  <section class="section" style="left:1306px;top:636px;height:239px">
    <h2 class="section-title">SEAFOOD</h2>
    <div class="row" style="top:86px"><span style="left:26px">CALAMARI RING</span><span style="left:229px">$2.00</span><span style="left:313px">CRAB STICK</span><span style="left:509px">$2.50</span></div>
    <div class="row" style="top:140px"><span style="left:26px">COCKTAIL FISH</span><span style="left:229px">$2.50</span><span style="left:313px">FISH CAKE</span><span style="left:509px">$3.50</span></div>
    <div class="row" style="top:194px"><span style="left:26px">PRAWN CUTLET</span><span style="left:229px">$2.50</span><span style="left:313px">BATTERED FISH</span><span style="left:509px">$7.00</span></div>
  </section>

  <section class="section" style="left:1306px;top:919px;height:420px">
    <h2 class="section-title">SEAFOOD PACK</h2>
    <div class="row small" style="top:89px"><span style="left:26px">TRADITIONAL</span><span style="left:514px">$9.00</span></div>
    <p class="note" style="left:26px;top:119px">Battered Fish &amp; Chip</p>
    <div class="row small" style="top:159px"><span style="left:26px">SNACKING PACK</span><span style="left:514px">$9.00</span></div>
    <p class="note" style="left:26px;top:189px">3 Cocktail Fish &amp; Chip</p>
    <div class="row small" style="top:228px"><span style="left:26px">FISHERMAN BASKET</span><span style="left:514px">$18.00</span></div>
    <p class="note" style="left:26px;top:258px">2 Calamari ring, 2 Prawn cutlet, 1 Crabstick, 1 Cocktail<br>Fish, Chip &amp; 1 can of soft drink</p>
    <div class="row small" style="top:321px"><span style="left:26px">FAMILY FEAST</span><span style="left:514px">$40.00</span></div>
    <p class="note" style="left:26px;top:351px">4 Prawn cutlets, 4 Calamari rings, 4 Crabstick, 6 cocktail<br>fish &amp; 1.25l bottle of soft drink</p>
  </section>

</div>
</body>
</html>
```